Website design for Keystone Bridge Advisory, a new boutique specialist consultancy company

We need a web design for a new company based in Australia called Keystone Bridge Advisory (this is abbreviated in our logo to KBA).

KBA is a boutique specialist advisory firm that provides Interim Management and Executive Transition Services. Through a suite of best practice methodologies coupled with advisory and consulting services, KBA supports businesses and executives during times of leadership hiatus and transition which not only mitigates risk of transition failure, but more importantly accelerates transition success.

Tobin at SketchHarbor has designed our logo (see attached file) and the logo and its colours will guide the website design. The primary colour scheme will be in the turquoise/aqua range and may include accent colours - designer's creative choice and guidance is welcome here.

The website should convey an image of crisp, modern professionalism. It's purpose will be to provide information about the company, our products and services and provide contact details. There is no online ordering or payment functionality required. Pages will include a home page with general information about the company, a number of content pages outlining information about each aspect of the services offered, an "about us" page and a "contact us" page.

Target Market(s)

This is a Busines-to-Business company and our target market is primarily large and medium sized companies. The specific individuals targeted at these companies will include:

Human Resources Directors
Talent and Recruitment Heads
Boards and Senior Executive teams of companies
Hiring managers responsible for recruiting and managing senior leaders and executives

Requirements
Should not have
• Online ordering / payment page

```html
<!DOCTYPE html>
<html lang="en">
<head>
<meta charset="utf-8">
<title>Keystone Bridge Advisory</title>
<link href="https://fonts.googleapis.com/css2?family=Didact+Gothic&family=Mulish:wght@400;600;700&display=swap" rel="stylesheet">
<style>
:root{
  --teal:#3cb8b5;
  --teal-dark:#178f8e;
  --orange:#e8522a;
  --text:#555;
  --heading:#1f9b99;
  --line:#dcdcdc;
  --panel:#f0f0f0;
}
*{box-sizing:border-box;margin:0;padding:0}
html,body{width:899px;height:1200px;overflow:hidden;background:#fff}
body{position:relative;font-family:"Didact Gothic",sans-serif;color:var(--text);font-size:10px}
.abs{position:absolute}
a{text-decoration:none;color:inherit}

/* header */
.brand{left:55px;top:13px;display:flex;align-items:center;gap:8px}
.brand-mark{font-family:"Mulish",sans-serif;font-weight:700;font-size:40px;color:var(--teal);letter-spacing:-1px;line-height:1}
.brand-name{border-left:1px solid var(--teal);padding-left:6px;color:var(--teal-dark);font-size:11.5px;line-height:12.5px;font-family:"Mulish",sans-serif}
.search{left:662px;top:26px;width:181px;height:27px;border:1px solid #d6d6d6;display:flex}
.search span{flex:1;padding:7px 10px;color:#aaa;font-size:9px}
.search b{width:27px;background:var(--orange);display:flex;align-items:center;justify-content:center}

/* nav */
.nav{left:0;top:75px;width:899px;height:36px;background:var(--teal)}
.nav ul{list-style:none;display:flex;position:absolute;left:55px;top:0;height:36px}
.nav li{color:#fff;font-size:10px;font-family:"Mulish",sans-serif;line-height:36px;padding:0 16px 0 0}
.nav li.active{background:var(--orange);padding:0 14px;margin-right:21px}
.nav li.sep{padding:0 18px 0 0}

/* hero */
.hero{left:55px;top:112px;width:788px;height:300px;border:2px solid #e2e2e2;
  background:linear-gradient(90deg,#e5f5ea 0%,#e8f4ee 40%,#c9cfd3 60%,#9aa3ab 100%)}
.hero h1{left:22px;top:70px;width:420px;font-family:"Mulish",sans-serif;font-weight:400;color:var(--orange);font-size:20.5px;line-height:29px}
.btn{display:inline-block;color:#fff;font-size:10.5px;font-family:"Mulish",sans-serif}
.hero .btn{left:22px;top:169px;background:var(--teal-dark);padding:7px 12px}
.dots{left:362px;top:263px;display:flex;gap:5px}
.dots i{width:12px;height:12px;border-radius:50%;background:#333}
.dots i:first-child{background:var(--teal-dark)}

/* sections */
h2{position:absolute;font-family:"Mulish",sans-serif;font-weight:400;color:var(--heading);font-size:18px}
.body-copy{line-height:17.5px;font-size:9.6px}
.rule{height:1px;background:var(--line)}
.btn-orange{background:var(--orange);padding:7px 11px}
.date{color:var(--orange);font-size:10px}
.news p{margin-top:6px;line-height:16px;font-size:9.6px}
.more{color:var(--heading);font-size:9.4px}
.photo{height:101px;width:182px}
.services{list-style:none}
.services li{height:23.5px;font-size:9.6px;display:flex;align-items:center;gap:12px}
.team{left:662px;top:704px;width:181px;height:241px;background:var(--panel)}
.arrows{font-size:14px;color:#333;letter-spacing:4px}
.client{width:114px;height:54px;border:1px solid #ddd;display:flex;align-items:center;justify-content:center;gap:6px;font-family:"Mulish",sans-serif;font-size:15px;color:#444}
.client i{width:14px;height:14px;border-radius:50%;background:var(--orange)}

/* footer */
.footer{left:0;top:1123px;width:899px;height:77px;background:var(--teal-dark);color:#fff}
.footer .mark{left:55px;top:12px;font-family:"Mulish",sans-serif;font-weight:700;font-size:26px;letter-spacing:-1px}
.footer .copy{left:55px;top:54px;font-size:8.5px}
.social{left:699px;top:28px;display:flex;align-items:center;gap:7px;font-size:9.5px}
.social i{width:22px;height:22px;border-radius:50%;display:block}
</style>
</head>
<body>

<header>
  <div class="abs brand">
    <div class="brand-mark">KBA</div>
    <div class="brand-name">Keystone<br>Bridge<br>Advisory Pty Ltd</div>
  </div>
  <div class="abs search">
    <span>Search...</span>
    <b><svg width="13" height="13" viewBox="0 0 13 13"><circle cx="5" cy="5" r="3.6" fill="none" stroke="#fff" stroke-width="1.6"/><line x1="7.6" y1="7.6" x2="12" y2="12" stroke="#fff" stroke-width="2"/></svg></b>
  </div>
</header>

<nav class="abs nav">
  <ul>
    <li class="active">HOME</li>
    <li class="sep">ABOUT US &nbsp;&nbsp;&nbsp;|</li>
    <li class="sep">SERVICES &nbsp;&nbsp;&nbsp;|</li>
    <li class="sep">OUR TEAM &nbsp;&nbsp;&nbsp;|</li>
    <li class="sep">LATEST NEWS &nbsp;&nbsp;&nbsp;|</li>
    <li class="sep">PROJECTS &nbsp;&nbsp;&nbsp;|</li>
    <li class="sep">BLOG &nbsp;&nbsp;&nbsp;|</li>
    <li class="sep">CLIENTS &nbsp;&nbsp;&nbsp;|</li>
    <li>CONTACT US</li>
  </ul>
</nav>

<section class="abs hero" role="img" aria-label="Business team working together around a laptop">
  <h1 class="abs">KBA is a boutique specialist advisory firm that provides Interim Management and Executive Transition Services</h1>
  <a class="abs btn" href="#">READ MORE ››</a>
  <div class="abs dots"><i></i><i></i><i></i><i></i></div>
</section>

<h2 style="left:55px;top:443px">Welcome to Our Website</h2>
<p class="abs body-copy" style="left:55px;top:474px;width:570px">Aliquam molestie, mi et imperdiet euismod, dui purus auctor tellus, et interdum lacus lectus et ante. Sed accumsan sollicitudin sapien, sit amet adipiscing turpis gravida ac. In congue, neque ac lobortis volutpat, libero mauris varius mi, vitae suscipit ipsum ligula vitae risus. Duis aliquam nibh a dui iaculis viverra id a velit. Vivamus egestas risus in magna varius commodo. Sed semper viverra egestas. Etiam pretium porttitor lectus, vel ornare neque porta volutpat.</p>
<a class="abs btn btn-orange" href="#" style="left:55px;top:559px">READ MORE ››</a>
<div class="abs rule" style="left:55px;top:601px;width:567px"></div>

<h2 style="left:55px;top:618px">Latest News</h2>
<article class="abs news" style="left:55px;top:653px;width:190px"><div class="date">Sep 23, 2014</div><p>Aliquam molestie, mi et imperdiet euismod, dui purus auctor tellus, et interdum lacus lectus et ante. Sed accumsan sollicitudin sapien, sit amet adipiscing turpis gravida ac...</p><a class="more" href="#" style="display:block;margin-top:5px">Learn More ››</a></article>
<article class="abs news" style="left:258px;top:653px;width:190px"><div class="date">Sep 23, 2014</div><p>Aliquam molestie, mi et imperdiet euismod, dui purus auctor tellus, et interdum lacus lectus et ante. Sed accumsan sollicitudin sapien, sit amet adipiscing turpis gravida ac...</p><a class="more" href="#" style="display:block;margin-top:5px">Learn More ››</a></article>
<article class="abs news" style="left:462px;top:653px;width:190px"><div class="date">Sep 23, 2014</div><p>Aliquam molestie, mi et imperdiet euismod, dui purus auctor tellus, et interdum lacus lectus et ante. Sed accumsan sollicitudin sapien, sit amet adipiscing turpis gravida ac...</p><a class="more" href="#" style="display:block;margin-top:5px">Learn More ››</a></article>
<div class="abs rule" style="left:55px;top:794px;width:567px"></div>

<h2 style="left:55px;top:808px">Our Projects</h2>
<div class="abs photo" role="img" aria-label="Colleagues collaborating at a desk" style="left:55px;top:844px;background:linear-gradient(135deg,#c9d9e6,#eef2f4 60%,#b8c6cf)"></div>
<div class="abs photo" role="img" aria-label="Two professionals in discussion" style="left:258px;top:844px;background:linear-gradient(135deg,#4f86b5,#dfe8ef 55%,#8fb0cc)"></div>
<div class="abs photo" role="img" aria-label="Hands reviewing charts on a tablet" style="left:460px;top:844px;background:linear-gradient(135deg,#2b3340,#8c97a3 55%,#d9dee3)"></div>

<h2 style="left:662px;top:443px">Our Services</h2>
<ul class="abs services" style="left:662px;top:471px;width:181px">
  <li><svg width="9" height="8" viewBox="0 0 9 8"><path d="M1 4l2.5 3L8 1" fill="none" stroke="#e8522a" stroke-width="1.8"/></svg>Aliquam molestie, mi et imperdiet</li>
  <li><svg width="9" height="8" viewBox="0 0 9 8"><path d="M1 4l2.5 3L8 1" fill="none" stroke="#e8522a" stroke-width="1.8"/></svg>Lectus et ante sed accumsan</li>
  <li><svg width="9" height="8" viewBox="0 0 9 8"><path d="M1 4l2.5 3L8 1" fill="none" stroke="#e8522a" stroke-width="1.8"/></svg>Sit amet adipiscing turpis gravida</li>
  <li><svg width="9" height="8" viewBox="0 0 9 8"><path d="M1 4l2.5 3L8 1" fill="none" stroke="#e8522a" stroke-width="1.8"/></svg>Neque ac lobortis volutpat</li>
  <li><svg width="9" height="8" viewBox="0 0 9 8"><path d="M1 4l2.5 3L8 1" fill="none" stroke="#e8522a" stroke-width="1.8"/></svg>Libero mauris varius mi</li>
  <li><svg width="9" height="8" viewBox="0 0 9 8"><path d="M1 4l2.5 3L8 1" fill="none" stroke="#e8522a" stroke-width="1.8"/></svg>Vitae suscipit ipsum ligula</li>
  <li><svg width="9" height="8" viewBox="0 0 9 8"><path d="M1 4l2.5 3L8 1" fill="none" stroke="#e8522a" stroke-width="1.8"/></svg>Duis aliquam nibh a dui iaculis</li>
  <li><svg width="9" height="8" viewBox="0 0 9 8"><path d="M1 4l2.5 3L8 1" fill="none" stroke="#e8522a" stroke-width="1.8"/></svg>Vivamus egestas risus in magna</li>
  <li><svg width="9" height="8" viewBox="0 0 9 8"><path d="M1 4l2.5 3L8 1" fill="none" stroke="#e8522a" stroke-width="1.8"/></svg>Sed semper viverra egestas</li>
</ul>

<aside class="abs team">
  <h2 style="left:17px;top:12px">Our Team</h2>
  <div class="abs arrows" style="left:144px;top:16px">‹›</div>
  <div class="abs" role="img" aria-label="Team member portrait" style="left:18px;top:44px;width:146px;height:105px;border:1px solid #ddd;background:linear-gradient(180deg,#f4f4f4,#d9d9d9)"></div>
  <div class="abs" style="left:18px;top:162px;color:var(--orange);font-size:12px">Daniel Hartley</div>
  <p class="abs" style="left:18px;top:180px;width:160px;line-height:16px;font-size:9.6px">Aliquam molestie, mi et imperdiet euismod, dui purus auctor tellus..</p>
  <a class="abs more" href="#" style="left:18px;top:219px">Learn More ››</a>
</aside>

<div class="abs rule" style="left:55px;top:970px;width:788px"></div>

<h2 style="left:55px;top:981px">Blog</h2>
<div class="abs arrows" style="left:401px;top:985px">‹›</div>
<div class="abs" style="left:55px;top:1016px;color:var(--orange);font-size:10px;font-weight:600">Nemo enim ipsam voluptatem voluptas sit aspernatur aut oditaut...</div>
<p class="abs" style="left:55px;top:1033px;width:370px;line-height:16px;font-size:9.6px">Aliquam molestie, mi et imperdiet euismod, dui purus auctor tellus, et interdum lacus lectus et ante. Sed accumsan sollicitudin sapien, sit amet adipiscing turpis gravida ac...</p>
<div class="abs" style="left:55px;top:1088px;color:var(--heading);font-size:9.6px">Posted on 23, 2014</div>

<h2 style="left:458px;top:983px">Clients</h2>
<div class="abs arrows" style="left:822px;top:985px">‹›</div>
<div class="abs client" style="left:460px;top:1022px"><i></i>Northwind</div>
<div class="abs client" style="left:595px;top:1022px"><i></i>Brightlane</div>
<div class="abs client" style="left:729px;top:1022px"><i></i>Corvale</div>

<footer class="abs footer">
  <div class="abs mark">KBA</div>
  <div class="abs copy">Copyright © 2014 Company Name. All Right Reserved</div>
  <div class="abs social">CONNECT US <i style="background:#3b5998;margin-left:4px"></i><i style="background:#2aa9e0"></i><i style="background:#f39c12"></i></div>
</footer>

</body>
</html>
```